PLUM- company with a mission

PLUM LLC stands for pure living under moonlight (non profit arm is called bright lantern foundation)—our business is based out of New York City and has a non-profit arm where for every bar you purchase, we donate a bar (don’t want any designs that limits us to only soap). Currently working with South Africa. We want the focus to be organic/natural soap with a mission.
What our website needs to…achieve:
Purpose = branding, building up interesting leaving up to launch date, then a full functional site for selling soap (for now) with a mission. With that said, there will need to be a page designed for “COMING SOON” – with a place to post our teaser 30 second video (kind of like a commercial/movie trailer) – until everything else is done.
We are the first in the industry to do one for one (or …50/50). Most companies that do charity work are mostly for every $$$ we donate $0.10, or 1% of XXX. We are starting out to run the non-profit arm as well not just after we reach certain milestones. In addition, we will be transparent for the non-profit side whereas most of the time when you donate, you have no idea where the money ends up going.
IN ADDITION: we still need to be clean/elegant – and selling our soap; so website will need to 1. Showcase our products, 2. Be very clear that we have a mission (not sure if there is a way to show case both our soap AND our mission)
Some sites we like:
Velbrook.com—like them in terms of business model—in terms of their website: like how their site is clean and friendly, but it seems too cluttered
www.quindelmarsh.com -- similar business model, www.pemaroux.com, kelvashop.com, ridgelybar.com
Duvik.com: like this a lot better than fernwicke.com, however, major dislike of the typeface. Okay about the neutral colors…although feel like we need something a bit more cheerful here and there for our mission
Zlabel.net, kelvashop.com, castlewren.com: like how they are clean and showcase well
**** However, our site also needs to convey messages like: www.feverfreeworld.org, www.cleanhandsunited.org
Looking for a clean, simple design. Modern, clutter-free, and inviting. Definitely do not want an arts and crafty/flowery feel. We do need something…cheerful for our nonprofit purposes.
Examples of sites we don’t like: marigoldhaus.com, petalpressbar.com
7 pages/ tabs maybe? (About us…video page (to show case what we are doing –currently my partner is in South Africa filming what our mission will be able to do – give children and those in need soap), FAQs, soap products, terms & conditions, contact us page, blog page……nothing too crazy).
For now, for designing purposes, please use any example texts whether it’s the about us page, mission page..policies.. and for the soap/products pages—please use example you can find online – it is fine, we just need the design done for now.
I have also attached our logo file. Please let me know if you have any questions! Thanks!
Something to consider....
velbrook.com and quindelmarsh.com are probably our largest competitor out of all the websites I mentioned as they have a very similar business model where it is is a company with a mission. Homepage makes that clear that for every pair of shoes/ glasses you purchase, they give a pair. Another thing to note...is that they have been in business for a few years so their website probably have changed to more commercial than focusing/marketing on the mission of doing good. While we don't want that to be the total focus, we do need it to be present on the homepage/front page.
Non-Profit

```html
<!DOCTYPE html>
<html lang="en">
<head>
<meta charset="utf-8">
<title>PLUM — Coming Soon</title>
<link rel="stylesheet" href="https://fonts.googleapis.com/css2?family=PT+Sans:wght@400;700&display=swap">
<style>
  :root {
    --sky-top: #86c9ee;
    --sky-mid: #cfe9f8;
    --sky-haze: #eef8fd;
    --sand-light: #f8dcaa;
    --sand: #f3c06c;
    --sand-deep: #efad45;
    --brand-orange: #f4a15c;
    --player-white: #ffffff;
    --player-grey: #8a8a8a;
    --track-grey: #7a7a7a;
    --progress-grey: #b5b5b5;
    --headline-light: #a8520f;
    --headline-dark: #6a2f05;
    --ink: #2b2b2b;
  }

  html, body {
    margin: 0;
    padding: 0;
    overflow: hidden;
  }

  body {
    width: 1200px;
    height: 883px;
  }

  .page {
    position: relative;
    width: 1200px;
    height: 883px;
    overflow: hidden;
    font-family: "PT Sans", Arial, sans-serif;
  }

  .page__scenery {
    position: absolute;
    inset: 0;
    background: linear-gradient(180deg,
      var(--sky-top) 0%,
      var(--sky-mid) 28%,
      var(--sky-haze) 44%,
      var(--sand-light) 50%,
      var(--sand) 68%,
      var(--sand-deep) 100%);
  }

  .brand-mark {
    position: absolute;
    left: 499px;
    top: 31px;
    width: 202px;
    height: 202px;
    border-radius: 50%;
    background: var(--brand-orange);
    display: flex;
    align-items: center;
    justify-content: center;
  }

  .brand-mark__name {
    font-family: "PT Sans", Arial, sans-serif;
    font-weight: 700;
    font-size: 60px;
    color: var(--player-white);
    letter-spacing: 2px;
  }

  .teaser-player {
    position: absolute;
    left: 231px;
    top: 259px;
    width: 738px;
    height: 408px;
    background: var(--player-white);
    border-radius: 3px;
    box-shadow: 0 1px 5px rgba(0, 0, 0, 0.3);
  }

  .teaser-player__play {
    position: absolute;
    left: 322px;
    top: 148px;
    width: 94px;
    height: 94px;
  }

  .teaser-player__controls {
    position: absolute;
    left: 24px;
    top: 360px;
    width: 692px;
    height: 26px;
    display: flex;
  }

  .controls__button {
    width: 37px;
    height: 26px;
    background: var(--brand-orange);
    display: flex;
    align-items: center;
    justify-content: center;
  }

  .controls__track {
    flex: 1;
    background: var(--track-grey);
    display: flex;
    align-items: center;
    padding: 0 10px;
  }

  .controls__bar {
    position: relative;
    width: 100%;
    height: 9px;
    background: var(--player-white);
  }

  .controls__progress {
    position: absolute;
    left: 0;
    top: 0;
    width: 46px;
    height: 9px;
    background: var(--progress-grey);
  }

  .launch-headline {
    position: absolute;
    left: 0;
    top: 681px;
    width: 1200px;
    margin: 0;
    text-align: center;
    font-family: "PT Sans", Arial, sans-serif;
    font-weight: 700;
    font-size: 66px;
    line-height: 1;
    letter-spacing: 1px;
    background: linear-gradient(180deg, var(--headline-light) 0%, var(--headline-dark) 100%);
    -webkit-background-clip: text;
    background-clip: text;
    color: transparent;
    filter: drop-shadow(0 1px 0 rgba(255, 255, 255, 0.7));
  }

  .social-follow {
    position: absolute;
    left: 458px;
    top: 779px;
    display: flex;
    align-items: center;
    gap: 6px;
  }

  .social-follow__label {
    font-size: 15px;
    color: var(--ink);
    margin-right: 6px;
  }

  .social-follow__link {
    display: block;
    width: 46px;
    height: 46px;
    border-radius: 50%;
    background: var(--player-white);
  }
</style>
</head>
<body>
  <main class="page">
    <div class="page__scenery" role="img" aria-label="Illustrated sunny sky with light rays, soft clouds and birds above rolling sandy hills"></div>

    <header class="brand-mark">
      <span class="brand-mark__name">PLUM</span>
    </header>

    <section class="teaser-player" aria-label="Teaser video">
      <svg class="teaser-player__play" viewBox="0 0 94 94" aria-hidden="true">
        <circle cx="47" cy="47" r="42" fill="none" stroke="var(--player-grey)" stroke-width="9"/>
        <polygon points="36,28 36,66 68,47" fill="var(--player-grey)"/>
      </svg>
      <div class="teaser-player__controls">
        <div class="controls__button">
          <svg width="12" height="14" viewBox="0 0 12 14" aria-hidden="true">
            <polygon points="0,0 0,14 12,7" fill="#ffffff"/>
          </svg>
        </div>
        <div class="controls__track">
          <div class="controls__bar"><div class="controls__progress"></div></div>
        </div>
        <div class="controls__button">
          <svg width="18" height="16" viewBox="0 0 18 16" aria-hidden="true">
            <rect x="1" y="1" width="11" height="9" fill="none" stroke="#ffffff" stroke-width="1.5"/>
            <rect x="7" y="6" width="10" height="9" fill="none" stroke="#ffffff" stroke-width="1.5"/>
          </svg>
        </div>
      </div>
    </section>

    <h1 class="launch-headline">COMING SOON</h1>

    <nav class="social-follow" aria-label="Follow us">
      <span class="social-follow__label">Follow Us</span>
      <a class="social-follow__link" href="#" aria-label="Social channel one"></a>
      <a class="social-follow__link" href="#" aria-label="Social channel two"></a>
      <a class="social-follow__link" href="#" aria-label="Video channel"></a>
    </nav>
  </main>
</body>
</html>
```